Halloway Crest Backers Guild business cards

Create a single-sided business card for the Halloway Crest Backers Guild based on the attached logo.
The additional data fields include Name, Title, Email, Phone, and website.
Please use the following as sample data:
Name: Dean Varrow
Title: Co-Founder / Investor
Email: deanvarrow@mailtern.net
Phone: 555-314-2706
Website: www.hcbackersguild.com

Target Market(s)

Start ups, entrepreneurs, venture capitalists

Industry/Entity Type

Investment

Contact Information for Business Card

Professional business card. Technology company.

Font styles to use
Serif
Sans Serif

Requirements
Must have
• Include the HCBG logo (attached)
• Name
• Title
• Email
• Phone
• Website
Should not have
• Cute, cartoony

```html
<!DOCTYPE html>
<html lang="en">
<head>
<meta charset="utf-8">
<title>Halloway Crest Backers Guild — Business Card</title>
<link rel="stylesheet" href="https://fonts.googleapis.com/css2?family=Open+Sans:wght@400&family=Barlow+Condensed:wght@400;500&display=swap">
<style>
  :root {
    --backdrop: #3b3b3b;
    --card-dark: #02030a;
    --card-light: #ffffff;
    --brand-green: #1e8a3e;
    --silver: #a3a3a6;
    --ink: #333333;
    --mist-green: #e1efe6;
    --mist-grey: #e6e6e6;
    --shadow: 0 6px 14px rgba(0,0,0,0.45);
  }
  * { margin: 0; padding: 0; box-sizing: border-box; }
  html, body {
    width: 1200px; height: 1200px; overflow: hidden;
    background: var(--backdrop);
  }
  .sheet { position: relative; width: 1200px; height: 1200px; }
  .card {
    position: absolute; left: 216px; width: 736px; height: 416px;
    box-shadow: var(--shadow); overflow: hidden;
  }
  .card--front { top: 154px; background: var(--card-dark); }
  .card--back { top: 630px; background: var(--card-light); }

  .wordmark {
    position: absolute; display: flex; align-items: center; gap: 22px;
    font-family: "Open Sans", sans-serif; font-weight: 400;
  }
  .wordmark__square { width: 20px; height: 20px; flex: none; }
  .wordmark__name { display: flex; flex-direction: column; }
  .wordmark__line1 { font-size: 35px; line-height: 1.05; letter-spacing: 1.5px; }
  .wordmark__line2 {
    font-size: 21px; line-height: 1.2; letter-spacing: 5px;
    text-transform: uppercase; margin-top: 2px;
  }
  .card--front .wordmark {
    left: 50%; top: 50%; transform: translate(-50%, -50%);
    color: var(--silver);
  }
  .card--front .wordmark__square { background: var(--silver); }
  .card--back .wordmark { left: 110px; top: 46px; color: var(--brand-green); }
  .card--back .wordmark__square { background: var(--brand-green); }

  .pattern-field {
    position: absolute; right: 0; top: 0; width: 340px; height: 416px;
    background:
      linear-gradient(to right, rgba(255,255,255,1) 0%, rgba(255,255,255,0) 35%),
      linear-gradient(160deg, var(--mist-green) 0%, var(--mist-grey) 45%, #f3f3f3 80%, #ffffff 100%);
  }

  .holder {
    position: absolute; left: 27px; top: 222px;
    font-family: "Barlow Condensed", sans-serif;
  }
  .holder__name { color: var(--brand-green); font-size: 34px; font-weight: 500; line-height: 1; }
  .holder__title { color: var(--ink); font-size: 22px; font-weight: 400; margin-top: 6px; }

  .contacts {
    position: absolute; left: 27px; top: 300px; list-style: none;
    font-family: "Barlow Condensed", sans-serif; font-size: 22px; color: var(--ink);
  }
  .contacts__item { display: flex; align-items: center; gap: 12px; height: 28px; }
  .contacts__icon { width: 22px; height: 18px; flex: none; }
</style>
</head>
<body>
<main class="sheet">
  <section class="card card--front" aria-label="Card front">
    <div class="wordmark">
      <span class="wordmark__square"></span>
      <span class="wordmark__name">
        <span class="wordmark__line1">Halloway Crest</span>
        <span class="wordmark__line2">Backers Guild</span>
      </span>
    </div>
  </section>

  <section class="card card--back" aria-label="Card back">
    <div class="pattern-field" role="img" aria-label="Faint green and grey dot pattern decoration"></div>

    <div class="wordmark">
      <span class="wordmark__square"></span>
      <span class="wordmark__name">
        <span class="wordmark__line1">Halloway Crest</span>
        <span class="wordmark__line2">Backers Guild</span>
      </span>
    </div>

    <div class="holder">
      <div class="holder__name">Dean Varrow</div>
      <div class="holder__title">Co-Founder / Investor</div>
    </div>

    <ul class="contacts">
      <li class="contacts__item">
        <svg class="contacts__icon" viewBox="0 0 22 18" aria-hidden="true">
          <path d="M1 7 Q11 -1 21 7 L18 9 L15 6 L7 6 L4 9 Z" fill="var(--brand-green)"/>
          <path d="M6 8 H16 L19 16 H3 Z" fill="var(--brand-green)"/>
          <circle cx="11" cy="12" r="2.4" fill="#fff"/>
        </svg>
        <span>555-314-2706</span>
      </li>
      <li class="contacts__item">
        <svg class="contacts__icon" viewBox="0 0 22 18" aria-hidden="true">
          <rect x="1" y="2" width="20" height="14" fill="var(--brand-green)"/>
          <path d="M2 3 L11 10 L20 3 M2 15 L8 8.5 M20 15 L14 8.5" stroke="#fff" stroke-width="1.6" fill="none"/>
        </svg>
        <span>deanvarrow@mailtern.net</span>
      </li>
      <li class="contacts__item">
        <svg class="contacts__icon" viewBox="0 0 22 22" aria-hidden="true">
          <g fill="none" stroke="var(--brand-green)" stroke-width="1.4">
            <circle cx="11" cy="11" r="9.5"/>
            <ellipse cx="11" cy="11" rx="4.2" ry="9.5"/>
            <path d="M11 1.5 V20.5 M1.5 11 H20.5 M3 6 H19 M3 16 H19"/>
          </g>
        </svg>
        <span>www.hcbackersguild.com</span>
      </li>
    </ul>
  </section>
</main>
</body>
</html>
```